Young and modern Electrical company working in the commercial arena.

Wanting a business card design thats modern and will last. Maybe Minimalist? Happy to look at changing my logo

Target Market(s)

Builders, Project Managers

Industry/Entity Type

Electrical

Contact Information for Business Card

Name
Address
Phone number
Job title

Logo Text

our name or just the logo i'm open to ideas

Font styles to use
Sans Serif

Requirements
Nice to have
• would like to keep the purple in our current logo. it's kinda unique to our market
Should not have
• Don't want it to be to busy. simple is best i think

```html
<!DOCTYPE html>
<html lang="en">
<head>
<meta charset="UTF-8">
<title>Brackwell Electrical – Business Card</title>
<link href="https://fonts.googleapis.com/css2?family=Exo+2:wght@500;600;700&family=Arimo:wght@400&display=swap" rel="stylesheet">
<style>
  :root {
    --page-bg: #e7e4df;
    --card-white: #ffffff;
    --card-dark: #0b0c12;
    --brand-purple: #6a55a8;
    --brand-lavender: #a79bd6;
    --accent-cyan: #1ea7dc;
    --ink: #1b1b1f;
    --ink-soft: #2b2b30;
    --faint-mark: #e9e9eb;
  }
  * { margin: 0; padding: 0; box-sizing: border-box; }
  html, body { width: 900px; height: 1200px; overflow: hidden; }
  body { background: var(--page-bg); position: relative; font-family: "Arimo", Arial, sans-serif; }

  .card {
    position: absolute;
    left: 82px;
    width: 740px;
    height: 432px;
    overflow: hidden;
    box-shadow: 0 6px 16px rgba(0,0,0,0.25);
  }
  .card--front {
    top: 125px;
    background: linear-gradient(180deg, #fbfbfb 0%, var(--card-white) 100%);
    border-radius: 46px 0 46px 0;
  }
  .card--back {
    top: 642px;
    background: var(--card-dark);
    border-radius: 0 46px 0 46px;
  }

  .brand-mark-circle {
    position: absolute;
    border-radius: 50%;
  }
  .card--front .brand-mark-circle {
    left: 51px; top: 48px; width: 114px; height: 114px;
    border: 6px solid var(--brand-purple);
  }
  .card--back .brand-mark-circle {
    left: 178px; top: 149px; width: 114px; height: 114px;
    border: 6px solid var(--brand-lavender);
  }

  .brand-name {
    position: absolute;
    font-family: "Exo 2", Arial, sans-serif;
    font-weight: 700;
    text-transform: uppercase;
    line-height: 1;
  }
  .brand-name span { display: block; }
  .brand-name .brand-name__primary { font-size: 36px; letter-spacing: 0.5px; }
  .brand-name .brand-name__secondary { font-size: 19px; letter-spacing: 9.5px; margin-top: 6px; }
  .card--front .brand-name { left: 183px; top: 74px; color: var(--brand-purple); }
  .card--back .brand-name { left: 312px; top: 176px; color: #ffffff; }

  .faint-mark {
    position: absolute;
    left: 470px; top: -30px;
    width: 300px; height: 300px;
    border-radius: 50%;
    border: 16px solid var(--faint-mark);
  }

  .holder-name {
    position: absolute;
    left: 48px; top: 282px;
    font-family: "Exo 2", Arial, sans-serif;
    font-weight: 600;
    font-size: 26px;
    color: var(--ink);
  }
  .holder-title {
    position: absolute;
    left: 48px; top: 313px;
    font-family: "Exo 2", Arial, sans-serif;
    font-weight: 500;
    font-size: 16px;
    letter-spacing: 0.6px;
    color: var(--brand-purple);
  }
  .title-rule {
    position: absolute;
    left: 234px; top: 327px;
    width: 454px; height: 2px;
    background: var(--brand-purple);
  }

  .contact-line {
    position: absolute;
    font-size: 16px;
    color: var(--ink-soft);
    display: flex;
    align-items: center;
    gap: 10px;
    line-height: 1;
  }
  .contact-line svg { width: 15px; height: 15px; fill: var(--accent-cyan); flex: none; }
  .contact-line--phone { left: 48px; top: 350px; }
  .contact-line--email { left: 48px; top: 373px; }
  .contact-line--address { right: 50px; top: 350px; }
  .contact-line--person { right: 76px; top: 373px; }
</style>
</head>
<body>

  <section class="card card--front" aria-label="Business card front">
    <div class="faint-mark" aria-hidden="true"></div>
    <div class="brand-mark-circle" aria-hidden="true"></div>
    <div class="brand-name">
      <span class="brand-name__primary">Brackwell</span>
      <span class="brand-name__secondary">Electrical</span>
    </div>

    <div class="holder-name">Owen Marsh</div>
    <div class="holder-title">Managing Director</div>
    <div class="title-rule"></div>

    <div class="contact-line contact-line--phone">
      <svg viewBox="0 0 24 24" aria-hidden="true"><path d="M6.6 10.8a15.1 15.1 0 0 0 6.6 6.6l2.2-2.2a1 1 0 0 1 1-.25 11.4 11.4 0 0 0 3.6.57 1 1 0 0 1 1 1V20a1 1 0 0 1-1 1A17 17 0 0 1 3 4a1 1 0 0 1 1-1h3.5a1 1 0 0 1 1 1c0 1.25.2 2.45.57 3.57a1 1 0 0 1-.25 1z"/></svg>
      <span>555.014.2277</span>
    </div>
    <div class="contact-line contact-line--email">
      <svg viewBox="0 0 24 24" aria-hidden="true"><path d="M2 5h20v14H2z"/><path d="M3 6.5 12 13l9-6.5" fill="none" stroke="#ffffff" stroke-width="1.6"/></svg>
      <span>owen@brackwellelectrical.com</span>
    </div>
    <div class="contact-line contact-line--address">
      <span>PO Box 41, Maplewood, PA 18000</span>
      <svg viewBox="0 0 24 24" aria-hidden="true"><path d="M12 2a7 7 0 0 0-7 7c0 5.2 7 13 7 13s7-7.8 7-13a7 7 0 0 0-7-7zm0 9.5A2.5 2.5 0 1 1 12 6.5a2.5 2.5 0 0 1 0 5z"/></svg>
    </div>
    <div class="contact-line contact-line--person">
      <span>Owen Marsh</span>
    </div>
  </section>

  <section class="card card--back" aria-label="Business card back">
    <div class="brand-mark-circle" aria-hidden="true"></div>
    <div class="brand-name">
      <span class="brand-name__primary">Brackwell</span>
      <span class="brand-name__secondary">Electrical</span>
    </div>
  </section>

</body>
</html>
```